Birch Flooring Supply

Basic one-sided business card design using the attached logo. Vintage americana theme. Font is modified Arial Nova Cond, but anything that coordinates can be used

```html
<!DOCTYPE html>
<html lang="en">
<head>
<meta charset="utf-8">
<title>Birch Flooring Supply – Business Card</title>
<link rel="stylesheet" href="https://fonts.googleapis.com/css2?family=Poppins:wght@400;600&family=Roboto:wght@700&display=swap">
<style>
  :root {
    --backdrop: #8b8b8b;
    --card-black: #070707;
    --kraft: #b89474;
    --white: #ffffff;
    --shadow: rgba(0, 0, 0, 0.55);
  }
  * { margin: 0; padding: 0; box-sizing: border-box; }
  html, body { width: 1093px; height: 1200px; overflow: hidden; }
  body { background: var(--backdrop); position: relative; font-family: "Poppins", sans-serif; }

  .card { position: absolute; box-shadow: 3px 4px 4px var(--shadow); }
  .card-front { left: 265px; top: 226px; width: 577px; height: 357px; background: var(--card-black); }
  .card-front .base-band { position: absolute; left: 0; right: 0; bottom: 0; height: 9px; background: var(--kraft); }
  .card-back { left: 265px; top: 620px; width: 582px; height: 357px; background: var(--kraft); }

  .holder { position: absolute; left: 26px; top: 45px; }
  .holder-name { font-family: "Roboto", sans-serif; font-weight: 700; font-size: 22.5px; color: var(--kraft); line-height: 1.1; letter-spacing: -0.2px; }
  .holder-title { font-size: 16.5px; color: var(--white); line-height: 1.2; }

  .contacts { position: absolute; left: 26px; top: 264px; list-style: none; }
  .contacts li { display: flex; align-items: center; gap: 7px; font-size: 17.5px; color: var(--white); line-height: 21px; }
  .contacts svg { width: 15px; height: 15px; flex: none; }

  .address { position: absolute; right: 33px; top: 285px; text-align: right; font-size: 17.5px; color: var(--white); line-height: 21px; }

  .brand-seal { position: absolute; border-radius: 50%; display: flex; align-items: center; justify-content: center; text-align: center; font-family: "Poppins", sans-serif; font-weight: 600; line-height: 1.15; }
  .card-front .brand-seal { left: 487px; top: 25px; width: 214px; height: 214px; margin-left: -193px; border: 3px solid var(--kraft); color: var(--white); font-size: 27px; padding: 20px; }
  .card-back .brand-seal { left: 177px; top: 66px; width: 226px; height: 226px; border: 3px solid var(--card-black); color: var(--card-black); font-size: 29px; padding: 20px; }
</style>
</head>
<body>
  <section class="card card-front">
    <div class="holder">
      <p class="holder-name">DANIEL HAYES</p>
      <p class="holder-title">Managing Director</p>
    </div>

    <div class="brand-seal">Birch Flooring Supply</div>

    <ul class="contacts">
      <li>
        <svg viewBox="0 0 16 16" aria-hidden="true"><path d="M4 1.5l2.5 3-1.5 1.8c.8 1.8 2.3 3.3 4.1 4.1l1.8-1.5 3 2.5-1.4 2.3C7.3 13.5 2.5 8.7 1.7 3z" fill="none" stroke="#fff" stroke-width="1.3"/></svg>
        044-987 654 321
      </li>
      <li>
        <svg viewBox="0 0 16 16" aria-hidden="true"><rect x="1" y="3.5" width="14" height="9" fill="#fff"/><path d="M1 3.5l7 5 7-5" fill="none" stroke="#070707" stroke-width="1.2"/></svg>
        info@birchflooring.com
      </li>
      <li>
        <svg viewBox="0 0 16 16" aria-hidden="true"><g fill="none" stroke="#fff" stroke-width="1.1"><circle cx="8" cy="8" r="6.5"/><ellipse cx="8" cy="8" rx="3" ry="6.5"/><path d="M1.5 8h13M2.5 4.8h11M2.5 11.2h11"/></g></svg>
        www.birchflooring.com
      </li>
    </ul>

    <p class="address">421, Address line goes here<br>45452,Country Name</p>

    <div class="base-band"></div>
  </section>

  <section class="card card-back">
    <div class="brand-seal">Birch Flooring Supply</div>
  </section>
</body>
</html>
```